A4 Childcare Spring Special Flyer

Crestwell Learning is a registered training organisation (RTO) Toid No. 47318, based in Blackburn, Victoria. We are a market leader in Professional development courses both accredited and non accredited, in order for you to maintain currency in your profession.

We need a flyer for a childcare specific spring special. The special is to offer a $50 VOLM gift card and 50% of your second training session. Conditions apply*

The training sessions available are the NEW childcare specific course: HLTAID004 Provide an emergency first aid response in an education and care setting and HLTAID003 Provide First Aid, HLTAID001 Provide Cardiopulmonary Resuscitation (CPR), 22024VIC Course in emergency management of asthma in the workplace
and 22099VIC Course in First Aid Management of Anaphylaxis.
We provide a flexible, cost effective and reliable service.
We have training locations available in Blackburn, Preston, Narre Warren and Mornington and can also provide onsite training.

We can also provide education and PRIVOS regulation consultation to the childcare provider.

Must use company logo, include phone number: (03) 5127 6481, website: www.crestwelllearning.com.au, email: marapenn@crestwelllearning.com.au

(Note that a letter with more detail will be attached with this flyer, therefore, with that in mind; use that information as desired).

The final product should be as childcare like as possible whilst also keeping our company colors (same as logo). We would also like for this flyer to stand out and be appealing to the recipient as this flyer is to gain potential clients, with emphasis on the HLTAID004 Course
Updates

Just need to update the qualifications: In the design brief I mentioned that the course; HLTAID001 Provide CPR and Asthma & Anaphyalxis.. Can this please be changed to HLTAID001 Provide Cardiopulmonary Resuscitation (CPR) And 22024VIC Course in emergency management of asthma in the workplace And 22099VIC Course in First Aid Management of Anaphylaxis (They are all singular courses) Apoligies!

Target Market(s)

Childcare centres, Out of school hours providers, pre-schools

Industry/Entity Type

Childcare

Font styles to use
Decorative

Colors
ffcf3e
f37123
faa54b

Requirements
Must have
• Company Logo
phone number
website
email
Registered Training Organisation
TOID: 47318

```html
<!DOCTYPE html>
<html lang="en">
<head>
<meta charset="utf-8">
<title>Crestwell Learning – Spring Special Courses</title>
<link rel="stylesheet" href="https://fonts.googleapis.com/css2?family=Arimo:wght@400;700&display=swap">
<style>
  :root {
    --sun: #ffcf3e;
    --tangerine: #f37123;
    --apricot: #faa54b;
    --flame: #e9592a;
    --ink: #2b2b2b;
    --white: #ffffff;
  }
  * { margin: 0; padding: 0; box-sizing: border-box; }
  html, body { width: 957px; height: 1200px; overflow: hidden; background: var(--white); }
  .flyer {
    position: relative;
    width: 957px;
    height: 1200px;
    overflow: hidden;
    font-family: "Arimo", Arial, sans-serif;
    color: var(--ink);
    background: linear-gradient(180deg, #f29a3c 0%, var(--apricot) 14%, #fbc07a 32%, #fde3bf 50%, #fff7ee 62%, var(--white) 70%);
  }
  .crowd-band {
    position: absolute;
    left: 0; top: 0;
    width: 957px; height: 125px;
    background: linear-gradient(180deg, #fbc56a 0%, #f7b352 70%, rgba(247,179,82,0) 100%);
  }
  .headline {
    position: absolute;
    left: 40px; top: 150px;
    color: var(--white);
    font-weight: 400;
    font-size: 32px;
    line-height: 30px;
    letter-spacing: 1.2px;
    text-transform: uppercase;
  }
  .feature-course {
    position: absolute;
    left: 38px; top: 229px;
    width: 600px; height: 95px;
    background: var(--white);
    padding: 10px 13px;
    color: var(--flame);
    font-weight: 700;
    font-size: 19.5px;
    line-height: 27px;
  }
  .offer-star { position: absolute; left: 545px; top: 0; width: 417px; height: 470px; }
  .offer-text {
    position: absolute;
    left: 622px; top: 145px;
    width: 300px;
    transform: rotate(15deg);
    transform-origin: center;
    color: var(--white);
    text-align: center;
    font-weight: 700;
  }
  .offer-title { font-size: 29px; letter-spacing: 2px; line-height: 36px; }
  .offer-detail { font-size: 18px; line-height: 23px; margin-top: 6px; }
  .offer-terms { font-size: 14px; margin-top: 18px; }
  .course-list {
    position: absolute;
    left: 40px; top: 340px;
    width: 880px;
    font-size: 20.5px;
    line-height: 26px;
    list-style: none;
  }
  .course-list li { display: flex; }
  .course-code { color: var(--tangerine); flex: none; }
  .course-code.hlt { width: 136px; }
  .course-code.vic { width: 131px; }
  .about {
    position: absolute;
    left: 50px; top: 494px;
    width: 860px;
    font-size: 20.5px;
    line-height: 25.5px;
  }
  .about p + p { margin-top: 25px; }
  .contact {
    position: absolute;
    right: 62px; top: 697px;
    text-align: right;
    font-style: normal;
    font-size: 21px;
    line-height: 30.5px;
  }
  .classroom-photo {
    position: absolute;
    left: -6px; top: 694px;
    width: 586px; height: 586px;
    border-radius: 50%;
    border: 15px solid var(--sun);
    background: radial-gradient(circle at 40% 45%, #e9dccd 0%, #c9a98a 40%, #8a6248 75%, #6c4a38 100%);
  }
  .brand {
    position: absolute;
    left: 643px; top: 850px;
    width: 220px;
    text-align: center;
    color: var(--tangerine);
    font-weight: 400;
    font-size: 40px;
    line-height: 38px;
  }
  .brand-dot {
    display: block;
    width: 120px; height: 120px;
    margin: 0 auto 52px;
    border-radius: 50%;
    background: var(--tangerine);
  }
  .rto {
    position: absolute;
    left: 583px; top: 1118px;
    width: 340px;
    text-align: center;
    font-size: 14px;
    line-height: 20px;
    color: var(--ink);
  }
</style>
</head>
<body>
<main class="flyer">
  <div class="crowd-band" role="img" aria-label="Silhouette of a cheering crowd with raised hands"></div>

  <h1 class="headline">Crestwell Learning<br>Spring Special Courses</h1>

  <div class="feature-course">NEW childcare specific course: HLTAID004<br>Provide an emergency first aid response in an<br>education and care setting</div>

  <svg class="offer-star" viewBox="0 0 417 470" aria-hidden="true">
    <polygon fill="#e9592a" points="247,22.5 263.8,175.2 409.7,223.5 269.7,286.8 268.8,440.4 165.4,326.8 19,373.4 95.1,240 5.5,115.1 156,146.3"/>
  </svg>
  <div class="offer-text">
    <div class="offer-title">SPECIAL OFFER</div>
    <div class="offer-detail">$50 VOLM gift card and<br>50% of your second<br>training session.</div>
    <div class="offer-terms">Conditions apply*</div>
  </div>

  <ul class="course-list">
    <li><span class="course-code hlt">HLTAID003</span>Provide First Aid</li>
    <li><span class="course-code hlt">HLTAID001</span><span>Provide Cardiopulmonary Resuscitation<br>(CPR)</span></li>
    <li><span class="course-code vic">22024VIC</span>Course in emergency management of asthma in the workplace</li>
    <li><span class="course-code vic">22099VIC</span>Course in First Aid Management of Anaphylaxis.</li>
  </ul>

  <div class="about">
    <p>We provide a flexible, cost effective and reliable service.<br>We have training locations available in Blackburn, Preston,<br>Narre Warren and Mornington and can also provide onsite training.</p>
    <p>We can also provide education and PRIVOS regulation consultation to the childcare<br>provider.</p>
  </div>

  <address class="contact">
    (03) 5127 6481<br>
    www.crestwelllearning.com.au<br>
    marapenn@crestwelllearning.com.au
  </address>

  <div class="classroom-photo" role="img" aria-label="Smiling educator with four young children at a classroom table"></div>

  <div class="brand">
    <span class="brand-dot"></span>
    crestwell<br>learning
  </div>

  <p class="rto">Registered Training Organisation<br>TOID: 47318</p>
</main>
</body>
</html>
```